Commercial Broker Profile Flyer

I need a one-page flyer created that will serve as a profile report for individual brokers within a commercial real estate firm. The flyer will include company branding, agent photo, bio, and other information. I would like to have the source file available for future editing preferably in a Publisher file format. A copy of a company brochure is included and would like to have this profile flyer similar to keep company branding consistent. Our company website is www.holbrookvalere.com for any other questions on branding.
Updates

Target Market(s)

Professional

Industry/Entity Type

Real Estate Agent

Requirements
Must have
• One page
• Source files MUST include a .PUB file that I can update in the future
• All of the information in the uploaded "content" file
• Company branding
• Must be 8.5"x11"
Should not have
• Do not use stock photos or property photos from the attachments. I only want the broker photo and company logo.

```html
<!DOCTYPE html>
<html lang="en">
<head>
<meta charset="utf-8">
<title>Broker Profile – T. Daniel Holbrook</title>
<link rel="stylesheet" href="https://fonts.googleapis.com/css2?family=Tinos:wght@400;700&family=Roboto+Condensed:wght@400&family=Arimo:wght@400&display=swap">
<style>
  :root {
    --brand-green: #15674a;
    --brand-green-soft: #cfe3d6;
    --paper: #ffffff;
    --backdrop: #808080;
    --ink: #222222;
    --photo-light: #b9bcbb;
    --photo-dark: #7f8483;
  }
  * { box-sizing: border-box; margin: 0; padding: 0; }
  html, body { width: 1200px; height: 1200px; overflow: hidden; }
  body { background: var(--backdrop); position: relative; font-family: "Arimo", Arial, sans-serif; color: var(--ink); }

  .flyer { position: absolute; left: 184px; top: 58px; width: 838px; height: 1084px; background: var(--paper); }
  .flyer > * { position: absolute; }

  .top-band { left: 0; top: 0; width: 838px; height: 62px; background: var(--brand-green); }
  .top-rule { left: 0; top: 66px; width: 838px; height: 3px; background: var(--brand-green); }
  .side-strip { left: 0; top: 82px; width: 35px; height: 952px; background: var(--brand-green); }
  .bottom-rule { left: 0; top: 1037px; width: 838px; height: 3px; background: var(--brand-green); }
  .bottom-band { left: 0; top: 1054px; width: 838px; height: 30px; background: var(--brand-green); }

  .broker-photo { left: 50px; top: 82px; width: 354px; height: 493px;
    background: radial-gradient(ellipse at 50% 35%, var(--photo-light), var(--photo-dark)); }

  .bio { left: 50px; top: 578px; width: 354px; height: 456px; background: var(--brand-green);
    padding: 22px 14px 0 12px; color: #fff; font-family: "Roboto Condensed", "Arial Narrow", sans-serif;
    font-size: 14.2px; line-height: 22.5px; letter-spacing: -0.1px; }
  .bio p + p { margin-top: 8px; }

  .flourish { left: 408px; top: 80px; width: 334px; height: 114px;
    background: linear-gradient(100deg, rgba(207,227,214,0) 0%, rgba(207,227,214,.8) 45%, rgba(207,227,214,.2) 100%);
    border-radius: 0 0 60px 0; }

  .brand { left: 428px; top: 220px; display: flex; align-items: center; gap: 14px; }
  .brand-mark { width: 82px; height: 82px; border-radius: 50%; background: var(--brand-green); flex: none; }
  .brand-name { font-family: "Arimo", Arial, sans-serif; font-weight: 400; color: var(--brand-green); font-size: 30px; line-height: 36px; }

  .broker-id { left: 434px; top: 376px; }
  .broker-name { font-family: "Tinos", "Times New Roman", serif; font-weight: 700; color: var(--brand-green); font-size: 17px; letter-spacing: .8px; }
  .broker-name small { font-size: 14px; }
  .broker-title { font-size: 16px; margin-top: 2px; }

  .contacts { left: 434px; top: 433px; list-style: none; font-size: 15.5px; }
  .contacts li { display: flex; align-items: center; gap: 8px; height: 23px; }
  .contacts svg { width: 16px; height: 16px; fill: var(--brand-green); flex: none; }

  .section-rule { left: 408px; top: 576px; width: 430px; height: 2px; background: var(--brand-green); }

  .panel { left: 433px; }
  .panel h2 { font-family: "Tinos", "Times New Roman", serif; font-weight: 700; color: var(--brand-green); font-size: 18.5px; }
  .clients { top: 604px; }
  .clients ul { list-style: none; margin-top: 8px; font-family: "Roboto Condensed", "Arial Narrow", sans-serif; font-size: 15px; }
  .clients li { display: flex; align-items: center; gap: 7px; height: 22.4px; }
  .clients svg { width: 16px; height: 16px; flex: none; }
  .affiliations { top: 876px; }
  .affiliations ul { list-style: none; margin-top: 8px; font-family: "Roboto Condensed", "Arial Narrow", sans-serif; font-size: 14.5px; line-height: 19.7px; }
</style>
</head>
<body>
<main class="flyer">
  <div class="top-band"></div>
  <div class="top-rule"></div>
  <div class="side-strip"></div>

  <div class="broker-photo" role="img" aria-label="Portrait photograph of the broker in a grey suit and striped tie"></div>

  <section class="bio">
    <p>Daniel began his real estate career in 2005 and has completed $75+ million in transactions representing sellers and buyers of commercial real estate, providing tenant representation, and leasing of retail and office properties. Prior to beginning his real estate career, Daniel served over five years in the Army Reserves and attended Piedmont State University.</p>
    <p>Daniel has earned the prestigious Certified Commercial Investment Advisor (CCIA) designation as well as the Certified Leasing Advisor (CLA) designation. Daniel is a member of the Global Council of Retail Centers (GCRC), the Carolina and Eastfield Realtor Association, the Eastfield-Larkin County Chamber of Commerce, and serves on the board of directors for the NC-CCIA Chapter, the Sandhill Community Center, and the Tallpine Realtors Association. Daniel is a licensed real estate broker in NC and SC.</p>
  </section>

  <div class="flourish" role="img" aria-label="Faint green decorative scroll ornament"></div>

  <div class="brand">
    <div class="brand-mark"></div>
    <p class="brand-name">Holbrook-Valere<br>Real Estate</p>
  </div>

  <div class="broker-id">
    <h1 class="broker-name">T. DANIEL HOLBROOK, <small>CCIA, CLA</small></h1>
    <p class="broker-title">Principal / Broker in Charge</p>
  </div>

  <ul class="contacts">
    <li><svg viewBox="0 0 16 16"><path d="M1 5c0-2 2-3 7-3s7 1 7 3v1h-4V4.5H5V6H1zM3 8l2-1.5h6L13 8v6H3z"/></svg>(555) 204-1617 ext. 202</li>
    <li><svg viewBox="0 0 16 16"><path d="M4 0h8v16H4zM5.5 2v10h5V2zM7 13.5h2v1H7z" fill-rule="evenodd"/></svg>(555) 318-5284</li>
    <li><svg viewBox="0 0 16 16"><path d="M1 3h14v10H1zM2 4.5v.3l6 4.2 6-4.2v-.3z" fill-rule="evenodd"/></svg>daniel@holbrookvalere.com</li>
    <li><svg viewBox="0 0 16 16"><circle cx="8" cy="8" r="7" fill="none" stroke="#15674a" stroke-width="1.5"/><path d="M1 8h14M8 1c-3 3.5-3 10.5 0 14M8 1c3 3.5 3 10.5 0 14" fill="none" stroke="#15674a" stroke-width="1.3"/></svg>www.holbrookvalere.com</li>
  </ul>

  <div class="section-rule"></div>

  <section class="panel clients">
    <h2>Clients Served</h2>
    <ul>
      <li><svg viewBox="0 0 16 16"><circle cx="8" cy="8" r="8" fill="#15674a"/><path d="M4.5 8.2l2.3 2.3 4.7-4.7" fill="none" stroke="#fff" stroke-width="2"/></svg>Hollow Creek Chicken</li>
      <li><svg viewBox="0 0 16 16"><circle cx="8" cy="8" r="8" fill="#15674a"/><path d="M4.5 8.2l2.3 2.3 4.7-4.7" fill="none" stroke="#fff" stroke-width="2"/></svg>Three Brothers Grill</li>
      <li><svg viewBox="0 0 16 16"><circle cx="8" cy="8" r="8" fill="#15674a"/><path d="M4.5 8.2l2.3 2.3 4.7-4.7" fill="none" stroke="#fff" stroke-width="2"/></svg>Trim Line Cuts</li>
      <li><svg viewBox="0 0 16 16"><circle cx="8" cy="8" r="8" fill="#15674a"/><path d="M4.5 8.2l2.3 2.3 4.7-4.7" fill="none" stroke="#fff" stroke-width="2"/></svg>Value Tread Tires</li>
      <li><svg viewBox="0 0 16 16"><circle cx="8" cy="8" r="8" fill="#15674a"/><path d="M4.5 8.2l2.3 2.3 4.7-4.7" fill="none" stroke="#fff" stroke-width="2"/></svg>Petite Bakes</li>
      <li><svg viewBox="0 0 16 16"><circle cx="8" cy="8" r="8" fill="#15674a"/><path d="M4.5 8.2l2.3 2.3 4.7-4.7" fill="none" stroke="#fff" stroke-width="2"/></svg>Crestway Healthcare</li>
      <li><svg viewBox="0 0 16 16"><circle cx="8" cy="8" r="8" fill="#15674a"/><path d="M4.5 8.2l2.3 2.3 4.7-4.7" fill="none" stroke="#fff" stroke-width="2"/></svg>Kinward Services</li>
      <li><svg viewBox="0 0 16 16"><circle cx="8" cy="8" r="8" fill="#15674a"/><path d="M4.5 8.2l2.3 2.3 4.7-4.7" fill="none" stroke="#fff" stroke-width="2"/></svg>Town Margin</li>
      <li><svg viewBox="0 0 16 16"><circle cx="8" cy="8" r="8" fill="#15674a"/><path d="M4.5 8.2l2.3 2.3 4.7-4.7" fill="none" stroke="#fff" stroke-width="2"/></svg>Bright Fizz Bottling</li>
    </ul>
  </section>

  <section class="panel affiliations">
    <h2>Professional Affiliations</h2>
    <ul>
      <li>Certified Commercial Investment Advisor (designee)</li>
      <li>Global Council of Retail Centers</li>
      <li>Tallpine Realtors Association</li>
      <li>Carolina Realtors Commercial Forms Committee</li>
    </ul>
  </section>

  <div class="bottom-rule"></div>
  <div class="bottom-band"></div>
</main>
</body>
</html>
```